larvosk.net

We are a IT Service for the valley. I want a clean website, with new Design, like animated pictures. We focus on IT. Give me your best design. What I'm looking for is eye catching. Works with Smart Phones, and iPad, Tab. Need a section for Submit a support tickets and Remote support. I'm looking for new ideals. I'm open mind, let me see what you guys can do.

Target Market(s)

My clients to see what service and products we have.

Industry/Entity Type

It Service

Requirements
Must have
• Able to submit a trouble tickets and works with Smart Phones, iPad, Tab.

```html
<!DOCTYPE html>
<html lang="en">
<head>
<meta charset="utf-8">
<title>Larvosk Technology – IT Service</title>
<link href="https://fonts.googleapis.com/css2?family=Open+Sans:wght@400;600;700&family=Questrial&display=swap" rel="stylesheet">
<style>
:root{
  --navy:#1f2a55;
  --red:#e41e26;
  --red-dark:#b3141a;
  --sky-1:#6fd3e3;
  --sky-2:#2a97c6;
  --ink:#1b1b1b;
  --grey-card:#3a3a3a;
  --footer:#3b3b3b;
  --footer-bar:#1e1e1e;
  --footer-text:#8c8c8c;
  --white:#ffffff;
  --teal-btn:#3aa3c9;
}
*{margin:0;padding:0;box-sizing:border-box}
html,body{width:836px;height:1200px;overflow:hidden;background:var(--white)}
body{position:relative;font-family:"Open Sans",sans-serif;color:var(--ink);font-size:10.5px;line-height:1.2}
.abs{position:absolute}
.brand{left:86px;top:40px;width:262px}
.brand-name{font-family:"Questrial",sans-serif;font-size:46px;color:var(--navy);letter-spacing:-1px;line-height:1}
.brand-sub{font-family:"Questrial",sans-serif;font-size:17px;letter-spacing:15.5px;color:var(--ink);margin-top:6px}
.tel-ribbon{left:597px;top:0;width:149px;height:76px}
.tel-text{left:597px;top:27px;width:149px;text-align:center;font-family:"Questrial",sans-serif;font-size:14px;color:#ffd9d0}
.main-nav{left:365px;top:92px;display:flex;font-family:"Questrial",sans-serif;font-size:11px;color:var(--ink)}
.main-nav span{padding:6px 12px;border-right:1px solid #c9d6de}
.main-nav span:last-child{border-right:none}
.hero{left:0;top:124px;width:836px;height:276px;background:radial-gradient(ellipse at 60% 30%,var(--sky-1),var(--sky-2) 85%);border-top:2px solid #1f7ea8}
.hero-art{left:88px;top:146px;width:234px;height:230px;border-radius:6px;background:linear-gradient(135deg,#e9eef1,#b8c6ce 60%,#1f3f85)}
.hero-title{left:391px;top:198px;font-family:"Questrial",sans-serif;font-weight:700;font-size:26px;color:#182238;letter-spacing:-0.8px;-webkit-text-stroke:0.6px #182238}
.hero-copy{left:392px;top:248px;width:320px;font-size:10.5px;color:#1c3a4e;line-height:1.2}
.hero-copy p{margin-bottom:12px}
.btn-red{background:var(--red);color:var(--white);font-weight:700;font-size:11px;padding:3px 8px;display:inline-block}
.hero-btn{left:392px;top:334px;font-size:12px;padding:4px 8px;border:1px solid var(--red-dark)}
.about-title{left:87px;top:413px;font-family:"Questrial",sans-serif;font-size:19px}
.about-copy{left:87px;top:453px;width:424px;font-size:10.5px;line-height:1.2}
.about-copy p{margin-bottom:12px}
.btn-teal{left:87px;top:611px;width:98px;height:26px;background:linear-gradient(#5ec0e0,var(--teal-btn));color:var(--white);font-weight:700;font-size:11.5px;text-align:center;line-height:26px;box-shadow:0 2px 3px rgba(0,0,0,.3)}
.ticket{left:533px;top:410px;width:209px;height:230px;background:var(--navy);border-radius:6px 6px 0 0;color:var(--white)}
.ticket h2{font-family:"Questrial",sans-serif;font-weight:400;font-size:19px;position:absolute;left:9px;top:3px}
.ticket .intro{position:absolute;left:10px;top:43px;width:185px;font-size:10.5px}
.field-label{position:absolute;font-size:10.5px;width:54px;text-align:right;left:0}
.field{position:absolute;left:59px;width:140px;height:23px;background:var(--white);border:1px solid #b9c2d0}
.select-arrow{position:absolute;right:0;top:0;width:27px;height:21px;border-left:1px solid #c9d0da}
.submit-wrap{left:510px;top:596px;width:178px;height:40px}
.submit-text{left:550px;top:600px;font-family:"Questrial",sans-serif;color:var(--white);font-size:17px;letter-spacing:.5px}
.card{width:209px;height:251px;background:var(--grey-card);color:var(--white);box-shadow:0 1px 3px rgba(0,0,0,.4)}
.card-art{height:105px}
.card h3{font-family:"Questrial",sans-serif;font-weight:400;font-size:14.5px;margin:9px 9px 6px}
.card p{margin:0 9px;font-size:10.5px;line-height:1.2}
.card .btn-red{margin:9px 0 0 9px}
.footer{left:0;top:945px;width:836px;height:220px;background:var(--footer);border-top:3px solid #2b89b5;color:var(--white)}
.footer h4{position:absolute;font-size:12px;font-weight:700;top:9px}
.hot-links{position:absolute;left:88px;top:40px;list-style:none;font-size:10.5px}
.hot-links li{position:relative;padding-left:11px;margin-bottom:12px;width:140px}
.hot-links li::before{content:"";position:absolute;left:0;top:3px;border-left:5px solid var(--red);border-top:4px solid transparent;border-bottom:4px solid transparent}
.quote{position:absolute;left:244px;width:320px;color:var(--footer-text);font-size:10.5px;line-height:1.2}
.quote cite{display:block;text-align:right;font-weight:700;font-style:italic;color:var(--white);margin-top:6px}
.tweet-brand{position:absolute;left:589px;top:37px;font-family:"Questrial",sans-serif;color:#3d4d84;font-size:25px;line-height:1}
.tweet-brand small{display:block;font-size:9.5px;letter-spacing:9px;color:#aaa;margin-top:2px}
.tweet{position:absolute;left:589px;width:160px;font-size:8.5px;color:#ddd;padding-left:24px}
.tweet::before{content:"";position:absolute;left:3px;top:1px;width:10px;height:10px;border-radius:50%;background:#e6e6e6}
.social{position:absolute;left:647px;top:177px;display:flex;gap:12px}
.social span{width:23px;height:23px;border-radius:50%;background:#d0d0d0}
.bottom-nav{left:0;top:1165px;width:836px;height:35px;background:var(--footer-bar);display:flex;justify-content:center;align-items:center;font-family:"Questrial",sans-serif;color:var(--white);font-size:11px}
.bottom-nav span{padding:8px 11px;border-right:1px solid #555}
.bottom-nav span:last-child{border-right:none}
</style>
</head>
<body>

<header>
  <div class="abs brand">
    <div class="brand-name">LARVOSK</div>
    <div class="brand-sub">TECHNOLOGY</div>
  </div>
  <svg class="abs tel-ribbon" viewBox="0 0 149 76" aria-hidden="true">
    <path d="M0 0H149V74L74.5 56L0 74Z" fill="#e41e26"/>
  </svg>
  <div class="abs tel-text">tel : (02) 555- 01942</div>
  <nav class="abs main-nav">
    <span>HOME</span><span>ABOUT US</span><span>OUR SERVICES</span><span>PRODUCTS</span><span>CONTACT US</span>
  </nav>
</header>

<section>
  <div class="abs hero"></div>
  <div class="abs hero-art" role="img" aria-label="Row of silver desktop monitors with blue screens"></div>
  <h1 class="abs hero-title">You can count on Our services.</h1>
  <div class="abs hero-copy">
    <p>Our team of technology experts work with you to deliver the best services and care the industry has to offer.</p>
    <p>Lorem Ipsum is simply dummy text of the printing and typesetting industry. Lorem Ipsum has been the industry's standard dummy text ever since the 1500s.</p>
  </div>
  <span class="abs btn-red hero-btn">Learn More</span>
</section>

<section>
  <h2 class="abs about-title">About Larvosk technology</h2>
  <div class="abs about-copy">
    <p>Lorem Ipsum is simply dummy text of the printing and typesetting industry. Lorem Ipsum has been the industry's standard dummy text ever since the 1500s, when an unknown printer took a galley of type and scrambled it to make a type specimen book. It has survived not only five centuries, but also the leap into electronic typesetting, remaining essentially unchanged. It was popularised in the 1960s with the release of Velmark sheets containing Lorem Ipsum passages, and more recently with desktop publishing software like Quillset Layout including versions of Lorem Ipsum.</p>
    <p>Lorem Ipsum is simply dummy text of the printing and typesetting industry. Lorem Ipsum has been the industry's standard dummy text ever since the 1500s.</p>
  </div>
  <div class="abs btn-teal">Learn More</div>

  <form class="abs ticket">
    <h2>Submit a ticket</h2>
    <p class="intro">Lorem Ipsum is simply dummy text of the printing and typesetting industry.</p>
    <span class="field-label" style="top:97px">Name :</span>
    <span class="field" style="top:93px"></span>
    <span class="field-label" style="top:128px">Email :</span>
    <span class="field" style="top:124px"></span>
    <span class="field-label" style="top:158px">IT pack :</span>
    <span class="field" style="top:154px">
      <span class="select-arrow"><svg width="27" height="21" viewBox="0 0 27 21" aria-hidden="true"><path d="M10 8h7l-3.5 5z" fill="#2a7fb5"/></svg></span>
    </span>
  </form>
  <svg class="abs submit-wrap" viewBox="0 0 178 40" aria-hidden="true">
    <path d="M0 20L24 12V38L4 38Z" fill="#a8131a"/>
    <path d="M23 0H170L178 8L168 30H23Z" fill="#e41e26"/>
  </svg>
  <div class="abs submit-text">SUBMIT NOW</div>
</section>

<section>
  <article class="abs card" style="left:87px;top:665px">
    <div class="card-art" role="img" aria-label="White puzzle pieces with one grey piece lifted over a red gap" style="background:linear-gradient(135deg,#f4f4f4,#d6d6d6)"></div>
    <h3>Business consulting</h3>
    <p>Lorem Ipsum is simply dummy text of the printing and typesetting industry. Lorem Ipsum has been the industry's standard dummy text ever since the 1500s, when an unknown printer took.</p>
    <span class="btn-red">Learn More</span>
  </article>
  <article class="abs card" style="left:308px;top:665px">
    <div class="card-art" role="img" aria-label="Glowing blue globe wrapped in network lines" style="background:radial-gradient(circle at 50% 60%,#cfefff,#2a7fd0 55%,#0b3b8a)"></div>
    <h3>Web solutions</h3>
    <p>Lorem Ipsum is simply dummy text of the printing and typesetting industry. Lorem Ipsum has been the industry's standard dummy text ever since the 1500s, when an unknown printer took.</p>
    <span class="btn-red">Learn More</span>
  </article>
  <article class="abs card" style="left:533px;top:665px">
    <div class="card-art" role="img" aria-label="Blue and white earth globe on a pale background" style="background:radial-gradient(circle at 45% 55%,#4a90c8,#8db8d6 45%,#e8eef2 70%)"></div>
    <h3>System managment</h3>
    <p>Lorem Ipsum is simply dummy text of the printing and typesetting industry. Lorem Ipsum has been the industry's standard dummy text ever since the 1500s, when an unknown printer took.</p>
    <span class="btn-red">Learn More</span>
  </article>
</section>

<footer>
  <div class="abs footer">
    <h4 style="left:88px">Hot Links</h4>
    <ul class="hot-links">
      <li>Lorem Ipsum is simply dummy text</li>
      <li>Lorem Ipsum is simply dummy text</li>
      <li>Lorem Ipsum</li>
      <li>Lorem Ipsum is simply</li>
      <li>simply dummy text</li>
    </ul>
    <h4 style="left:246px">Testimonials</h4>
    <blockquote class="quote" style="top:41px">Lorem Ipsum is simply dummy text of the printing and typesetting industry. Lorem Ipsum has been the industry's standard dummy text ever since the 1500s, when an unknown printer took a galley of type and scrambled<cite>Elena R.</cite></blockquote>
    <blockquote class="quote" style="top:126px">Lorem Ipsum is simply dummy text of the printing and typesetting industry. Lorem Ipsum has been the industry's standard dummy text ever since the 1500s, when an unknown printer took a galley of type and scrambled<cite>Tomas V.</cite></blockquote>
    <h4 style="left:589px">Latest tweets</h4>
    <div class="tweet-brand">LARVOSK<small>TECHNOLOGY</small></div>
    <p class="tweet" style="top:94px">Lorem Ipsum is simply dummy text of the printing and typesetting industry.</p>
    <p class="tweet" style="top:138px">Lorem Ipsum is simply dummy text of the printing and typesetting industry.</p>
    <div class="social" aria-hidden="true"><span></span><span></span><span></span></div>
  </div>
  <nav class="abs bottom-nav">
    <span>HOME</span><span>ABOUT US</span><span>OUR SERVICES</span><span>PRODUCTS</span><span>CONTACT US</span>
  </nav>
</footer>

</body>
</html>
```